Become a Mentor - For Musicians, Artists, Producers and Teachers

Here is the full creative brief:

https://files.plenwick.com/sheets/d/4kTqpLm8Wz_2RNa7Hc3Xv91Jd0Gb5YeUsQ6fNo8rTpxa/view?mode=shared

Here is the background image file: https://www.trovecrate.com/sh/83jbwtrmq5dkx2u/BBHn4k7QTf2ZpLeXX-wr9MUHe?dl=0

LOGO:
https://www.trovecrate.com/sh/k472rufmpdo9b6w/BBKLe3RtHY5J-sFQnLZw7Ggma?dl=0

```html
<!DOCTYPE html>
<html lang="en">
<head>
<meta charset="utf-8">
<title>Become a Mentor – Meridian School of Music</title>
<link rel="stylesheet" href="https://fonts.googleapis.com/css2?family=Montserrat:wght@300;400;800&family=Lato:wght@400;700&family=Oswald:wght@500&display=swap">
<style>
  :root {
    --page: #e9e6e1;
    --ink: #0a0a10;
    --white: #ffffff;
    --cyan: #74d6f2;
    --cyan-deep: #1f9bd8;
    --blue-light: #8fdcf7;
    --magenta: #d8145f;
    --magenta-dark: #b00d4c;
    --photo-a: #5d5a58;
    --photo-b: #2b2a2c;
    --photo-c: #8a7d70;
    --muted: #c9c9d2;
  }
  * { box-sizing: border-box; margin: 0; padding: 0; }
  html, body { width: 1200px; height: 880px; overflow: hidden; background: var(--page); }
  .flyer {
    position: absolute; left: 310px; top: 30px; width: 580px; height: 820px;
    background: radial-gradient(ellipse at 40% 62%, #2a1530 0%, var(--ink) 60%);
    overflow: hidden; color: var(--white);
    font-family: "Lato", sans-serif;
    box-shadow: 0 6px 22px rgba(0,0,0,.18);
  }
  .flyer__shapes { position: absolute; inset: 0; }
  .brand {
    position: absolute; left: 24px; top: 362px;
    display: flex; align-items: center; gap: 10px;
    font-family: "Montserrat", sans-serif; font-weight: 800;
    font-size: 17px; line-height: 1.1; color: var(--white); letter-spacing: .04em;
  }
  .brand__dot { width: 34px; height: 34px; border-radius: 50%; background: var(--cyan-deep); flex: none; }
  .headline { position: absolute; left: 26px; top: 462px; font-family: "Montserrat", sans-serif; }
  .headline__lead { font-weight: 300; font-size: 36px; line-height: 40px; letter-spacing: .02em; }
  .headline__main { font-weight: 800; font-size: 42px; line-height: 50px; color: var(--cyan); letter-spacing: .01em; }
  .intro { position: absolute; left: 26px; top: 596px; font-size: 18.5px; line-height: 24px; }
  .contact { position: absolute; left: 34px; top: 680px; width: 340px; }
  .contact__icon { position: absolute; left: 0; top: 12px; width: 58px; height: 58px; }
  .contact__label {
    position: absolute; left: 72px; top: 0;
    font-family: "Montserrat", sans-serif; font-weight: 400;
    font-size: 24px; letter-spacing: .2em; color: var(--cyan);
  }
  .contact__phone {
    position: absolute; left: 72px; top: 26px;
    font-family: "Oswald", sans-serif; font-weight: 500; font-size: 46px; line-height: 56px;
  }
  .contact__web { position: absolute; left: 0; top: 94px; font-size: 17px; font-weight: 700; white-space: nowrap; }
  .contact__web span { color: var(--cyan); font-weight: 400; }
  .divider { position: absolute; left: 374px; top: 690px; height: 100px; border-left: 2px dotted var(--muted); }
  .apply {
    position: absolute; left: 400px; top: 700px; width: 142px; height: 36px;
    border-radius: 18px; background: linear-gradient(180deg, var(--magenta), var(--magenta-dark));
    display: flex; align-items: center; gap: 10px; padding-left: 8px;
    font-weight: 700; font-size: 16px; color: var(--white);
  }
  .apply__play { width: 24px; height: 24px; }
  .social { position: absolute; left: 440px; top: 762px; display: flex; gap: 32px; }
  .social__square { width: 24px; height: 24px; border-radius: 3px; background: #3b5aa5; }
  .social__square--alt { background: #c8367a; }
</style>
</head>
<body>
<main class="flyer">
  <svg class="flyer__shapes" viewBox="0 0 580 820" width="580" height="820">
    <defs>
      <linearGradient id="photoTone" x1="0" y1="0" x2="1" y2="1">
        <stop offset="0" stop-color="var(--photo-c)"/>
        <stop offset=".45" stop-color="var(--photo-a)"/>
        <stop offset="1" stop-color="var(--photo-b)"/>
      </linearGradient>
      <linearGradient id="prism" x1="0" y1="0" x2="1" y2="1">
        <stop offset="0" stop-color="var(--blue-light)"/>
        <stop offset="1" stop-color="var(--cyan-deep)"/>
      </linearGradient>
    </defs>
    <polygon role="img" aria-label="Photo: two music producers talking in a recording studio beside a mixing desk"
             points="0,0 580,0 580,298 250,388 0,262" fill="url(#photoTone)"/>
    <polygon points="250,381 580,298 580,547" fill="url(#prism)"/>
    <polygon points="330,360 580,298 580,420" fill="var(--blue-light)" opacity=".45"/>
    <polygon points="420,410 580,330 580,547" fill="var(--cyan-deep)" opacity=".35"/>
  </svg>

  <div class="brand"><span class="brand__dot"></span><span>MERIDIAN<br>SCHOOL OF MUSIC</span></div>

  <h1 class="headline">
    <span class="headline__lead">START YOUR<br>CAREER TODAY</span><br>
    <span class="headline__main">BECOME A MENTOR</span>
  </h1>

  <p class="intro">Turn your skills and passion for music into a career<br>Design for Musicians,Artists Producers and Teachers</p>

  <div class="contact">
    <svg class="contact__icon" viewBox="0 0 58 58" aria-hidden="true">
      <circle cx="29" cy="29" r="26" fill="none" stroke="var(--cyan)" stroke-width="3"/>
      <path d="M20 16c2-1 4 0 5 2l2 5c.5 1.5 0 3-1 4l-2 1c1.5 3.5 4 6 7.5 7.5l1-2c1-1 2.5-1.5 4-1l5 2c2 1 3 3 2 5l-1 2c-1 2-3 3-5 2.5-9-2-17-10-19-19-.5-2 .5-4 2.5-5z" fill="var(--white)"/>
    </svg>
    <div class="contact__label">CALL US NOW</div>
    <div class="contact__phone">130.055.2418</div>
    <div class="contact__web">www.<span>meridianschoolofmusic</span>.com.au</div>
  </div>

  <div class="divider"></div>

  <div class="apply">
    <svg class="apply__play" viewBox="0 0 24 24" aria-hidden="true">
      <circle cx="12" cy="12" r="11" fill="var(--white)"/>
      <polygon points="9,7 17,12 9,17" fill="var(--magenta)"/>
    </svg>
    Apply Now
  </div>

  <div class="social">
    <span class="social__square"></span>
    <span class="social__square social__square--alt"></span>
  </div>
</main>
</body>
</html>
```